Web Design for Solar Energy Consultancy Company

~ May 3, 2017 Update ~
As our project is rapidly progressing towards its completion, we started building up the list of designs that attracted the most of the team's attention. Additional submittals are still most welcome. Before submitting your proposal, however, we can recommend to review the concepts that received 4 stars as these are the ones that, in our opinion, most closely match the brief's requirements. Thank you!!
~ April 30, 2017 Update ~
The project deadline has been extended to attract a broader design community and to better tailor the final design to the requirements of the project.
A "light", "clean" (minimalistic), professionally looking, unique design is expected. Please, try to avoid industry cliches. Also, please use green, which became another industry cliche, with great caution. The brief provides minimum details to foster creativity. With the same notion in mind, the page content information is not provided.
Thank you for your feedback and support of the project!!
~ April 22, 2017 Update ~
Additional comments after starting receiving more designs:
- your attention to the brief's requirements will be highly appreciated. It is expected that the design is unique - standard, commonly used, images, formats and approaches do not fall under this category. There is no need to "bombard" with slightly different variations of the same design. It is expected that a conceptual (preliminary) design is submitted first, and, after it is reviewed (each design will receive a star rating and, if the star rating is greater than 3, a detailed feedback), the requested changes are implemented. We believe this will allow to approach the design process more efficiently and safe additional time to both the Designers's Community and our company. Thank you for understanding.
Clarification, please submit two variations of a design:
1) 1 page "business card" design that the company will be able to use during its startup stage;
2) the fully functional design (as per the requirements outlined below) for the company to transition to after the start-up period is over. Same design principles as developed for option 1 should be used for this variation.
Additional clarification, please note that the news block will not require images (at least during the start-up stage). It is envisioned to be a news feeder.
~ April 21, 2017 Update ~
Preliminary comments after receiving first designs:
- please try to create a unique design, using common elements wisely. Though such solar energy "attributes" as a solar panel or a bulb are very well recognized and allow quickly identify the nature of the business, they also became so common that in many cases a design may seem very similar to the one of others (Oh!, I've already seen this... effect).
- please try to introduce the company's logo unobtrusively. The size and position of the logo should clearly identify the company, but the message should be subtle, the logo should not distract from the main design. Brask's swoosh did not need to occupy have the screen.
- please use the green color with caution as it was with the company's logo. True, it is a green energy. But there is no need for the color to "scream" about it. Use the amount of green and its tone (avoid acid green) wisely.
--------------------------------------------------------------------------------
1. Main Goal
Develop a website that can represent the company to the industry stakeholders and become its "business card" during the start-up stage.
2. Secondary Goal
Develop a structure of a fully functional website that the "business card" design can eventually be transformed to staying consistent with the original design principles.
3. Key Audience
Varolu Corp. is providing consulting and technical services in the area of Solar Energy. The industry stakeholders include project developers, financial community, governmental bodies, OEMs, and competition.
4. Site Map
- HOME
• About
• Services
• Solar Energy
• News
• Contacts
• Social Media
- SERVICES*
- PROJECTS*
- FINANCE*
- TRAINING*
- SOLAR (ENERGY)*
* Maybe inactive / partially functional during the start-up stage.
5. Technical Specifications
Online brochure website during the start-up stage with a capability to be eventually transformed to a fully functional website while preserving the original design principles.
The design to be appealing, "light", professional, and with an intuitive and easy to navigate interface. Modern coding principles supporting efficiency and security to be utilized. Newest industry trends in website coding will be welcome.
The website to be designed so that it would fit well a computer, tablet, or mobile phone screen of any size. Cross-platform functionality to be taken into consideration to ensure that the website is fully functional on any platform.
Company's logo has already been designed and will be shared with the short-listed designers during the final design stage.
6. Interaction
The website will provide information about the company, our services, and projects. In addition, the industry insight, accumulated knowledge, and most recent trends are planned to be shared with stakeholders and attract and retain the audience.
Interaction with designers during the website development is envisioned to go through the following steps:
a) conceptual design - to be proposed by a designer originally. All conceptual designs will be reviewed and a feedback provided to pre-selected designers;
b) (preliminary and) final design - depending on the level of additional changes required can be broken into two steps. After discussing preliminary designs, company images will be provided to the selected finalists, who will compete with their final proposals.
7. Industry Stakeholders
- https://www.quellbrin.com/power/solar-power.- http://www.pakortavon.com/
- http://www.vellitrazo.com/about/company/
- https://www.oruxem.com/energy/index.html
8. Budget
Defined by the project.
9. Timescale
Defined by the project.
12. Additional Info
- No copy-cats, standard graphics, or cliches please!
- Additional information / clarifications will be gladly provided upon request.
- This specification may be updated throughout the project to reflect discussions with / changes proposed by the Designers community.

```html
<!DOCTYPE html>
<html lang="en">
<head>
<meta charset="utf-8">
<title>Varolu Corp. — Solar Energy Consulting</title>
<link rel="stylesheet" href="https://fonts.googleapis.com/css2?family=Lato:wght@400;700&family=Open+Sans:wght@400;600&display=swap">
<style>
:root{
  --orange:#f5a10f;
  --orange-dark:#e48a00;
  --green:#12ad4b;
  --ink:#2b2b2b;
  --body:#555;
  --muted:#777;
  --band:#f2f2f2;
  --line:#dcdcdc;
  --white:#fff;
}
*{box-sizing:border-box;margin:0;padding:0}
html,body{width:1200px;height:2429px;overflow:hidden;background:var(--white)}
body{font-family:"Open Sans",Arial,sans-serif;color:var(--body);position:relative}
.abs{position:absolute}
.heading{font-family:"Lato",Arial,sans-serif;font-weight:400;color:var(--ink);letter-spacing:3px;text-transform:uppercase}

/* header */
.site-header{top:0;left:0;width:1200px;height:105px;background:var(--white)}
.brand{display:flex;align-items:center;gap:10px;font-family:"Lato",sans-serif;font-weight:700;color:#444;letter-spacing:2px}
.brand .dot{border-radius:50%;background:var(--orange)}
.site-header .brand{left:133px;top:28px;font-size:30px}
.site-header .brand .dot{width:46px;height:46px}
.main-nav{top:50px;right:133px;display:flex;gap:58px;font-family:"Lato",sans-serif;font-size:12px;letter-spacing:1.2px;color:#222}
.main-nav .active{color:var(--orange)}

/* hero */
.hero{top:105px;left:0;width:1200px;height:450px;
  background:linear-gradient(180deg,#6b5a4a 0%,#c0763a 25%,#f3b23a 55%,#f7c94a 68%,#3a3d48 72%,#1d2028 100%)}
.hero-title{top:210px;width:1200px;text-align:center;color:var(--white);font-size:38px;letter-spacing:3px;font-family:"Lato",sans-serif}
.hero-sub{top:286px;width:1200px;text-align:center;color:#fff4e0;font-size:18px;letter-spacing:.6px}
.btn-quote{top:339px;left:509px;width:182px;height:52px;background:var(--orange);color:var(--white);border-radius:3px;display:flex;align-items:center;justify-content:center;font-family:"Lato",sans-serif;font-size:13px;letter-spacing:1px}
.hero-dots{top:513px;left:584px;display:flex;gap:6px}
.hero-dots span{width:11px;height:11px;border-radius:50%;background:#333}
.hero-dots span:first-child{background:var(--orange)}

.btn-green{background:var(--green);color:var(--white);border-radius:3px;display:flex;align-items:center;justify-content:center;font-family:"Lato",sans-serif;font-size:11px;letter-spacing:1px}

/* welcome */
.welcome-title{top:608px;width:1200px;text-align:center;font-size:36px}
.welcome-text{top:673px;left:185px;width:830px;text-align:center;font-size:11.5px;line-height:24px}
.welcome .btn-green{top:779px;left:542px;width:116px;height:35px}

/* services */
.services{top:890px;left:0;width:1200px;height:666px;background:var(--band)}
.services-title{top:50px;width:1200px;text-align:center;font-size:35px}
.service-card{top:144px;width:278px;height:442px;background:var(--white)}
.service-card .photo{width:278px;height:189px}
.service-card h3{margin-top:30px;text-align:center;font-size:20px}
.service-card p{margin:22px auto 0;width:240px;text-align:center;font-size:11.5px;line-height:24px}
.service-card .btn-green{margin:27px auto 0;width:96px;height:34px}

/* news */
.news-title{top:1618px;width:1200px;text-align:center;font-size:35px}
.news-item{top:1718px;width:440px;height:140px;display:flex;gap:25px}
.news-item .photo{width:166px;height:140px;flex:none}
.news-item h4{font-size:20px;margin-top:0}
.news-item p{margin:14px 0 0 6px;font-size:11.5px;line-height:24px;width:250px}
.news-item .more{margin:10px 0 0 8px;font-size:11px;color:#333;letter-spacing:.8px}

/* partners */
.partner{top:1945px;width:288px;height:112px;border:1px solid var(--line);display:flex;align-items:center;justify-content:center;gap:10px;font-family:"Lato",sans-serif;font-size:24px;color:#4a4a4a}
.partner .mark{width:22px;height:22px;background:#9aa0a6}

/* footer */
.site-footer{top:2110px;left:0;width:1200px;height:319px;background:var(--band)}
.site-footer .brand{left:133px;top:45px;font-size:32px}
.site-footer .brand .dot{width:70px;height:70px}
.social{left:133px;top:134px;display:flex;gap:8px}
.social span{width:32px;height:32px;border-radius:50%;border:1.5px solid #888}
.footer-head{font-family:"Lato",sans-serif;font-size:14px;color:#333;letter-spacing:.5px}
.quick{left:424px;top:30px}
.quick ul{list-style:none;margin-top:22px;font-size:11px;line-height:24px;color:#666}
.newsletter{left:596px;top:30px;width:252px}
.newsletter p{margin-top:20px;font-size:10.5px;line-height:24px;color:#666}
.newsletter .field{margin-top:12px;height:40px;background:var(--white);border:1px solid var(--line);font-size:10.5px;color:#555;padding:12px 16px}
.newsletter .btn-green{margin-top:14px;width:82px;height:28px;font-size:10px;letter-spacing:.3px}
.contact{left:904px;top:30px;width:170px}
.contact ul{list-style:none;margin-top:20px;font-size:11px;color:#666}
.contact li{display:flex;gap:12px;margin-bottom:11px;line-height:16px}
.contact svg{flex:none;margin-top:2px}
.contact .mail{text-decoration:underline}
.footer-rule{left:133px;top:264px;width:934px;height:1px;background:var(--line)}
.copyright{top:286px;width:1200px;text-align:center;font-size:10.5px;color:#666}
</style>
</head>
<body>

<header class="site-header abs">
  <div class="brand abs"><span class="dot"></span>VAROLU</div>
  <nav class="main-nav abs">
    <span class="active">HOME</span><span>SERVICES</span><span>PROJECTS</span><span>FINANCE</span><span>TRAINING</span><span>SOLAR</span>
  </nav>
</header>

<section class="hero abs" role="img" aria-label="Sunset sky over rows of solar panels">
</section>
<h1 class="hero-title abs">SOLAR ENERGY CONSULTING</h1>
<p class="hero-sub abs">Varolu Corp. is providing consulting and technical services in the area of Solar Energy.</p>
<div class="btn-quote abs">REQUEST QUOTE</div>
<div class="hero-dots abs"><span></span><span></span><span></span></div>

<section class="welcome">
  <h2 class="welcome-title heading abs">Welcome to Varolu</h2>
  <p class="welcome-text abs">Nemo enim ipsam voluptatem quia voluptas sit aspernatur aut odit aut fugit, sed quia consequuntur magni dolores eos qui ratione voluptatem sequi nesciunt. Neque porro quisquam est, qui dolorem ipsum quia dolor sit amet, consectetur, adipisci velit, sed quia non numquam eius modi tempora incidunt ut labore et dolore magnam aliquam quaerat voluptatem.</p>
  <div class="btn-green abs">READ MORE</div>
</section>

<section class="services abs">
  <h2 class="services-title heading abs">Our Services</h2>
  <article class="service-card abs" style="left:133px">
    <div class="photo" role="img" aria-label="Engineer in a hard hat looking over a solar array" style="background:linear-gradient(160deg,#cfe6f7,#7fb6e0 60%,#3f7fc0)"></div>
    <h3 class="heading">Projects</h3>
    <p>Nemo enim ipsam voluptatem quia voluptas sit aspernatur aut odit aut fugit, sed quia consequuntur</p>
    <div class="btn-green">READ MORE</div>
  </article>
  <article class="service-card abs" style="left:461px">
    <div class="photo" role="img" aria-label="Close-up of solar panel cells at sunset" style="background:linear-gradient(170deg,#c9874a,#6b4a3a 45%,#22242e)"></div>
    <h3 class="heading">Finance</h3>
    <p>Nemo enim ipsam voluptatem quia voluptas sit aspernatur aut odit aut fugit, sed quia consequuntur</p>
    <div class="btn-green">READ MORE</div>
  </article>
  <article class="service-card abs" style="left:788px">
    <div class="photo" role="img" aria-label="Worker installing solar panels on a roof" style="background:linear-gradient(180deg,#3b7fd0,#6da2dd 45%,#3a4658 70%,#c0603a)"></div>
    <h3 class="heading">Training</h3>
    <p>Nemo enim ipsam voluptatem quia voluptas sit aspernatur aut odit aut fugit, sed quia consequuntur</p>
    <div class="btn-green">READ MORE</div>
  </article>
</section>

<section class="news">
  <h2 class="news-title heading abs">Recent News</h2>
  <article class="news-item abs" style="left:133px">
    <div class="photo" role="img" aria-label="Solar panels in a green field under blue sky" style="background:linear-gradient(180deg,#3f86d6,#8cbbe8 45%,#2f3c52 60%,#4f9a3a)"></div>
    <div>
      <h4 class="heading">Projects</h4>
      <p>Nemo enim ipsam voluptatem quia voluptas sit aspernatur aut odit aut fugit, sed quia consequuntur</p>
      <div class="more">Read More &gt;&gt;</div>
    </div>
  </article>
  <article class="news-item abs" style="left:636px">
    <div class="photo" role="img" aria-label="Solar panels and wind turbines in a field" style="background:linear-gradient(180deg,#7aaee0,#d9e8f5 40%,#34425a 62%,#5aa040)"></div>
    <div>
      <h4 class="heading">Projects</h4>
      <p>Nemo enim ipsam voluptatem quia voluptas sit aspernatur aut odit aut fugit, sed quia consequuntur</p>
      <div class="more">Read More &gt;&gt;</div>
    </div>
  </article>
</section>

<section class="partners">
  <div class="partner abs" style="left:133px"><span class="mark"></span>Pakortavon</div>
  <div class="partner abs" style="left:457px"><span class="mark"></span>Oruxem</div>
  <div class="partner abs" style="left:778px"><span class="mark"></span>Vellitrazo</div>
</section>

<footer class="site-footer abs">
  <div class="brand abs"><span class="dot"></span>VAROLU</div>
  <div class="social abs"><span></span><span></span><span></span><span></span><span></span></div>

  <div class="quick abs">
    <div class="footer-head">QUICK LINKS</div>
    <ul><li>HOME</li><li>SERVICES</li><li>PROJECTS</li><li>FINANCE</li><li>TRAINING</li><li>SOLAR</li></ul>
  </div>

  <div class="newsletter abs">
    <div class="footer-head">NEWSLETTER</div>
    <p>Enter your email address to receive the latest news and notes from our blog.</p>
    <div class="field">Enter Your Mail Id</div>
    <div class="btn-green">SUBSCRIBE</div>
  </div>

  <div class="contact abs">
    <div class="footer-head">CONTACT US</div>
    <ul>
      <li><svg width="12" height="12" viewBox="0 0 12 12"><path d="M2 1h2l1 3-1.5 1a7 7 0 0 0 3.5 3.5L8 7l3 1v2a1 1 0 0 1-1 1A9 9 0 0 1 1 2a1 1 0 0 1 1-1z" fill="#666"/></svg>(555) 013-4100</li>
      <li><svg width="12" height="12" viewBox="0 0 12 12"><rect x="3" y="1" width="6" height="3" fill="#666"/><rect x="1" y="4" width="10" height="5" fill="#666"/><rect x="3" y="7" width="6" height="4" fill="#fff" stroke="#666"/></svg>(555) 013-4100</li>
      <li><svg width="12" height="12" viewBox="0 0 12 12"><rect x="1" y="2.5" width="10" height="7" fill="#666"/><path d="M1 3l5 3.5L11 3" stroke="#fff" fill="none"/></svg><span class="mail">info@varolumail.com</span></li>
      <li><svg width="12" height="12" viewBox="0 0 12 12"><path d="M6 11S2 6.8 2 4.5a4 4 0 0 1 8 0C10 6.8 6 11 6 11z" fill="#666"/><circle cx="6" cy="4.5" r="1.4" fill="#fff"/></svg>#2868 Lorem ipsum dolor sit amet, consectetur</li>
    </ul>
  </div>

  <div class="footer-rule abs"></div>
  <div class="copyright abs">©2017 Varolu. All rights reserved.</div>
</footer>

</body>
</html>
```